Harbourline Lodgings letterhead

We need a letterhead designed that includes the new logo that has just been designed for our business. The letterhead will need to be formatted for digital use as well as for print.

Target Market(s)

Private tenant, corporate tenants, real estate agents

Industry/Entity Type

Digital

Requirements
Must have
• ABN 57 918 402 263
PO Box 7186, Dunmore Mail Centre QLD 4803
Email: marlow.tidewell@postnest.com
Ph: 0438 562 094

```html
<!DOCTYPE html>
<html lang="en">
<head>
<meta charset="utf-8">
<title>Harbourline Lodgings Letterhead</title>
<link rel="stylesheet" href="https://fonts.googleapis.com/css2?family=Arimo:wght@400;700&display=swap">
<style>
  :root {
    --brand-red: #7a2b25;
    --brand-maroon: #5e1a2b;
    --ink: #222222;
    --paper: #ffffff;
  }
  * { margin: 0; padding: 0; box-sizing: border-box; }
  html, body { width: 928px; height: 1200px; overflow: hidden; background: var(--paper); }
  body { font-family: "Arimo", Arial, sans-serif; color: var(--ink); }
  .letterhead { position: relative; width: 928px; height: 1200px; background: var(--paper); overflow: hidden; }

  .brand { position: absolute; left: 30px; top: 30px; display: flex; align-items: center; gap: 14px; }
  .brand-mark { width: 22px; height: 22px; background: var(--brand-maroon); border-radius: 4px; }
  .brand-name { color: var(--brand-red); font-weight: 700; font-size: 26px; line-height: 1.1; letter-spacing: 0.5px; text-transform: uppercase; }

  .contact-block { position: absolute; left: 432px; top: 32px; font-size: 12.5px; line-height: 1; }
  .contact-line { display: flex; align-items: center; gap: 8px; height: 20px; }
  .contact-line .icon { width: 14px; height: 14px; flex: none; fill: var(--brand-maroon); }
  .contact-line--address { padding-left: 6px; }
  .contact-line--email { margin-top: 5px; }
  .contact-web { display: block; margin-top: 3px; color: var(--brand-red); font-weight: 700; font-size: 12.5px; }

  .divider { position: absolute; left: 737px; top: 34px; width: 2px; height: 46px; background: var(--brand-red); }

  .contact-side { position: absolute; left: 749px; top: 36px; font-size: 12.5px; }
  .phone-line { display: flex; align-items: center; gap: 8px; padding-left: 12px; }
  .phone-line .icon { width: 20px; height: 20px; flex: none; }
  .abn-line { margin-top: 10px; color: var(--ink); }
  .abn-line .label { color: var(--brand-red); }

  .footer-wave { position: absolute; left: 0; top: 1060px; width: 928px; height: 140px; }
  .footer-web { position: absolute; left: 623px; top: 1151px; color: var(--paper); font-size: 16px; }
</style>
</head>
<body>
<main class="letterhead">
  <header>
    <div class="brand">
      <span class="brand-mark"></span>
      <span class="brand-name">Harbourline<br>Lodgings</span>
    </div>

    <div class="contact-block">
      <div class="contact-line contact-line--address">
        <svg class="icon" viewBox="0 0 14 14" aria-hidden="true"><path d="M7 0C4.2 0 2.2 2 2.2 4.7 2.2 8 7 14 7 14s4.8-6 4.8-9.3C11.8 2 9.8 0 7 0zm0 6.6a2 2 0 1 1 0-4 2 2 0 0 1 0 4z"/></svg>
        <span>PO Box 7186, Dunmore Mail Centre QLD 4803</span>
      </div>
      <div class="contact-line contact-line--email">
        <svg class="icon" viewBox="0 0 16 12" aria-hidden="true" style="width:18px"><path d="M0 2 8 7l8-5V12H0z"/><path d="M0 0h16v1L8 6 0 1z"/></svg>
        <span>marlow.tidewell@postnest.com</span>
      </div>
      <span class="contact-web">www.harbourlinelodgings.com</span>
    </div>

    <div class="divider"></div>

    <div class="contact-side">
      <div class="phone-line">
        <svg class="icon" viewBox="0 0 20 20" aria-hidden="true">
          <circle cx="10" cy="10" r="9" fill="none" stroke="var(--brand-maroon)" stroke-width="1.5"/>
          <path d="M6.5 5.5l2 -0.5 1 2.3-1.2 1a6 6 0 0 0 2.6 2.6l1-1.2 2.3 1-.5 2c-4 .4-7.6-3.2-7.2-7.2z" fill="var(--brand-maroon)"/>
        </svg>
        <span>0438 562 094</span>
      </div>
      <div class="abn-line"><span class="label">ABN</span> : 57 918 402 263</div>
    </div>
  </header>

  <footer>
    <svg class="footer-wave" viewBox="0 1060 928 140" aria-hidden="true">
      <path d="M0 1124 C80 1168 200 1186 330 1186 C560 1184 760 1122 928 1108 L928 1200 L0 1200 Z" fill="var(--brand-red)"/>
      <path d="M60 1183 C330 1190 620 1142 928 1124" fill="none" stroke="var(--paper)" stroke-width="3"/>
    </svg>
    <span class="footer-web">www.harbourlinelodgings.com</span>
  </footer>
</main>
</body>
</html>
```